Kneadwell Bodycare

We are a Massage Therapy business based in Invercargill, New Zealand. We specialise in Sports and deep tissue massage but also provide relaxation and aromatherapy massage. We would like to see designs that use the the logo.
The final design should promote health and fitness.
Updates

Hi I am getting feedback that my business card picture is poor quality. I got this picture from plaza press under massage. So if you google this image a better quality picture should come up,. If not hope to upload a better image by tomorow, thanks.

Target Market(s)

Sports, people with pain and injuries

Industry/Entity Type

Massage

Requirements
Must have
• Logo, muscle body that is used on the business card, also a poster that matches my business card
Nice to have
• Picture of muscle man, shown on my business card
Should not have
• Not a picture of a real person

```html
<!DOCTYPE html>
<html lang="en">
<head>
<meta charset="utf-8">
<title>Kneadwell Bodycare – Are You In Pain?</title>
<link href="https://fonts.googleapis.com/css2?family=Bebas+Neue&family=Barlow+Condensed:ital,wght@1,600&family=Open+Sans:wght@400&family=Oswald:wght@500&display=swap" rel="stylesheet">
<style>
  :root {
    --ink: #4b5660;
    --teal: #2fa9c2;
    --paper: #ffffff;
    --muscle-light: #f0b9a2;
    --muscle-mid: #d9765a;
    --muscle-deep: #b8432e;
  }
  * { margin: 0; padding: 0; box-sizing: border-box; }
  html, body { width: 848px; height: 1200px; overflow: hidden; background: var(--paper); }
  .poster { position: relative; width: 848px; height: 1200px; overflow: hidden; background: var(--paper); }

  .anatomy-art { position: absolute; left: 0; top: 0; width: 520px; height: 1010px; }

  .headline {
    position: absolute; top: 40px; left: 170px; width: 640px;
    font-family: "Bebas Neue", sans-serif; font-size: 118px; line-height: 1;
    color: var(--ink); text-align: center; letter-spacing: 1px;
  }

  .brand {
    position: absolute; top: 258px; left: 228px; width: 400px;
    display: flex; align-items: center; justify-content: center; gap: 14px;
  }
  .brand-name { font-family: "Open Sans", sans-serif; font-size: 36px; color: var(--teal); }
  .brand-dot { width: 22px; height: 22px; border-radius: 50%; background: var(--teal); }

  .offer { position: absolute; left: 466px; font-family: "Barlow Condensed", sans-serif; font-style: italic; font-weight: 600; }
  .offer-services { top: 410px; }
  .offer-prices { top: 686px; }
  .offer-title { color: var(--teal); font-size: 28px; line-height: 42px; text-transform: uppercase; }
  .offer-list { list-style: none; }
  .offer-list li { color: var(--ink); font-size: 28px; line-height: 43px; text-transform: uppercase; }
  .offer-list li::before { content: "•"; margin-right: 10px; font-style: normal; }

  .footer-wave { position: absolute; left: 0; top: 0; width: 848px; height: 1200px; }

  .contact { position: absolute; left: 43px; top: 1040px; color: var(--ink); }
  .contact-phone { display: flex; align-items: center; gap: 10px; font-family: "Oswald", sans-serif; font-weight: 500; font-size: 46px; line-height: 56px; }
  .contact-line { font-family: "Open Sans", sans-serif; font-size: 23px; line-height: 38px; }
</style>
</head>
<body>
<div class="poster">

  <svg class="anatomy-art" viewBox="0 0 520 1010" role="img" aria-label="Anatomical illustration of a muscular back, shoulder and upper arm with red pain highlights">
    <defs>
      <linearGradient id="muscleTone" x1="0" y1="0" x2="1" y2="1">
        <stop offset="0" stop-color="var(--muscle-light)"/>
        <stop offset="0.55" stop-color="var(--muscle-mid)"/>
        <stop offset="1" stop-color="var(--muscle-deep)"/>
      </linearGradient>
    </defs>
    <path d="M0 0 H115 C105 120 160 250 255 330 C360 390 420 520 445 720 L475 1010 H0 Z" fill="url(#muscleTone)"/>
  </svg>

  <h1 class="headline">Are You In Pain?</h1>

  <div class="brand">
    <span class="brand-name">Kneadwell Bodycare</span>
    <span class="brand-dot"></span>
  </div>

  <section class="offer offer-services">
    <h2 class="offer-title">Kneadwell Bodycare</h2>
    <ul class="offer-list">
      <li>Deep Tissue</li>
      <li>Sports Massage</li>
      <li>Relaxation</li>
      <li>Aromatherapy</li>
      <li>Hot Stones</li>
    </ul>
  </section>

  <section class="offer offer-prices">
    <h2 class="offer-title">Prices</h2>
    <ul class="offer-list">
      <li>30Minutes $40</li>
      <li>60Minutes $60</li>
      <li>90 Minutes $80</li>
    </ul>
  </section>

  <svg class="footer-wave" viewBox="0 0 848 1200" aria-hidden="true">
    <path d="M848 825 C700 900 420 960 0 975 L0 1200 L848 1200 Z" fill="var(--teal)"/>
    <path d="M848 880 C680 945 420 985 0 990 L0 1200 L848 1200 Z" fill="var(--paper)"/>
  </svg>

  <address class="contact" style="font-style:normal">
    <div class="contact-phone">
      <svg width="52" height="40" viewBox="0 0 52 40" aria-hidden="true">
        <path d="M4 14 C4 4 48 4 48 14 L48 18 L36 18 L36 12 C30 9 22 9 16 12 L16 18 L4 18 Z" fill="var(--ink)"/>
        <path d="M12 20 L40 20 L46 38 L6 38 Z" fill="var(--ink)"/>
        <circle cx="26" cy="29" r="5" fill="var(--paper)"/>
      </svg>
      <span>0271846205</span>
    </div>
    <p class="contact-line">48 Marlow St, Invercargill 9810</p>
    <p class="contact-line">Clara Hewitt Bachelor Therapeiutic &nbsp;&amp; Sports massage</p>
  </address>

</div>
</body>
</html>
```